Bref créative
Quiet Harbor Dental Urgent Clinic- Business Cards and Stationary
Quiet Harbor Dental Urgent Clinic
Professional
Peter Delacroix, Jr., DMD
Founder/ CEO
2718 Pellam Rd
Ste 412
Houston, TX 77291
1-855-GRIN-WELLS
petedx4@mailvane.example
www.GRINWELLS.example
we can see you now!
RED, WHITE AND BLUE
I Have raised the $$$$ for postcard fabrication as well. let's get it!
attached is the graphic concept i'd like to achieve with the postcard.

```html
<!DOCTYPE html>
<html lang="en">
<head>
<meta charset="utf-8">
<title>Quiet Harbor Dental Urgent Clinic – Postcard</title>
<link href="https://fonts.googleapis.com/css2?family=Playfair+Display:wght@400;700&display=swap" rel="stylesheet">
<style>
  :root {
    --page: #ffffff;
    --card: #ffffff;
    --ink: #1c1c1c;
    --red: #c4242b;
    --navy: #1d3f7a;
    --grey: #8a8a8a;
    --photo-light: #f1f2f2;
    --photo-mid: #d9dcdc;
    --photo-green: #cfe6b8;
    --shadow: rgba(0,0,0,0.22);
  }
  * { margin: 0; padding: 0; box-sizing: border-box; }
  html, body {
    width: 1200px; height: 422px; overflow: hidden;
    background: var(--page);
    font-family: "Playfair Display", Georgia, serif;
  }
  .spread { position: relative; width: 1200px; height: 422px; }
  .card {
    position: absolute; top: 19px; width: 564px; height: 389px;
    background: var(--card);
    box-shadow: 0 2px 6px var(--shadow);
    overflow: hidden;
  }
  .card--front { left: 19px; }
  .card--back { left: 618px; }

  .photo-area {
    position: absolute; inset: 0;
    background:
      radial-gradient(ellipse at 45% 30%, var(--photo-green) 0%, rgba(207,230,184,0) 40%),
      linear-gradient(160deg, var(--photo-light) 0%, var(--photo-mid) 100%);
  }

  .headline {
    position: absolute; left: 88px; top: 266px;
    color: var(--ink); text-transform: uppercase; line-height: 1;
    letter-spacing: 0.5px;
  }
  .headline span { display: block; }
  .headline .line-1 { font-size: 23px; }
  .headline .line-2 { font-size: 27px; margin-top: 2px; }
  .headline .line-3 { font-size: 20px; margin-top: 3px; }
  .headline .line-4 { font-size: 22px; margin-top: 3px; }
  .headline .accent { color: var(--red); display: inline; }
  .headline .big { font-size: 30px; }

  .brand {
    position: absolute; left: 0; right: 0; top: 164px;
    display: flex; align-items: center; justify-content: center; gap: 10px;
  }
  .brand-dot { width: 34px; height: 34px; border-radius: 50%; background: var(--navy); flex: none; }
  .brand-name {
    font-size: 17px; font-weight: 700; color: var(--navy);
    text-transform: uppercase; line-height: 1.1; letter-spacing: 0.5px;
  }
  .tagline {
    position: absolute; left: 0; right: 0; top: 214px; text-align: center;
    font-size: 9px; color: var(--red); text-transform: uppercase; letter-spacing: 1px;
  }
  .contact {
    position: absolute; left: 0; right: 0; top: 338px; text-align: center;
    font-size: 10px; letter-spacing: 2px; color: var(--grey); line-height: 1.8;
  }
</style>
</head>
<body>
<main class="spread">
  <section class="card card--front">
    <div class="photo-area" role="img" aria-label="Photo of a calendar page with a dentist appointment written on it and a green and white toothbrush lying across"></div>
    <h1 class="headline">
      <span class="line-1">A R<span class="accent">EVO</span>LUTIONARY</span>
      <span class="line-2">Approach</span>
      <span class="line-3">To<span class="accent">the</span>same of</span>
      <span class="line-4"><span class="accent big">Tooth</span> ache</span>
    </h1>
  </section>

  <section class="card card--back">
    <div class="brand">
      <span class="brand-dot"></span>
      <span class="brand-name">Quiet Harbor<br>Dental Urgent Clinic</span>
    </div>
    <p class="tagline">We can see you now!</p>
    <p class="contact">1-855-GRIN-WELLS<br>www.GRINWELLS.example</p>
  </section>
</main>
</body>
</html>
```